Ember Pipe, EXCITING NEW HOOKAH BAR IN AKRON OHIO

I'd like a design for a Hookah Lounge that I just opened.We'd like to portray a Modern take on Tradition Hookah.We have 3 Outdoor Patios, one being reserved for VIP, we just secured Our Liqour license, so we hope to start serving next month.We provide a Traditional Hookah Experience in a Modern Enviorment.We use alot of warmer colors such as deep red, deep blue, and black.You can visit us on Facebook and Instagram to see what we are all about.. Company name Ember Pipe in Akron OhioThis is the link for our prototype website: http://plorvane.com/epbx/There you may use any artwork you see.
Target Market(s)
18 years and older. New smokers to seasoned smokers. We are here for everyone.
Contact Information for Business Card
Isaac Friga330.869.21401288 Weathervane Lane, Akron OH 40927

```html
<!DOCTYPE html>
<html lang="en">
<head>
<meta charset="utf-8">
<title>Ember Pipe – Business Card</title>
<link href="https://fonts.googleapis.com/css2?family=Montserrat:wght@400;600;800&display=swap" rel="stylesheet">
<style>
  :root {
    --backdrop: #e9e7e4;
    --ember-red: #dc1f26;
    --deep-red: #b8161c;
    --card-black: #1c1c1e;
    --row-line: #3a3a3d;
    --icon-blue: #1e5fae;
    --ink-light: #f1f1ee;
    --ink-muted: #d9d9d6;
  }
  * { box-sizing: border-box; margin: 0; padding: 0; }
  html, body {
    width: 1200px; height: 1000px; overflow: hidden;
    background: var(--backdrop);
    font-family: "Montserrat", sans-serif;
  }
  .card {
    position: absolute; left: 250px;
    width: 700px; height: 400px;
    overflow: hidden;
    box-shadow: 0 10px 24px rgba(0,0,0,.22);
  }
  .card--front { top: 70px; background: var(--ember-red); }
  .card--back { top: 530px; display: flex; }

  .front__band {
    position: absolute; left: 0; right: 0; top: 104px; height: 192px;
    background: var(--card-black);
    display: flex; align-items: center; justify-content: center;
  }
  .wordmark {
    display: flex; align-items: center; gap: 14px;
    color: var(--ink-light); font-weight: 800;
    letter-spacing: 4px; text-transform: uppercase;
  }
  .wordmark__dot { width: 18px; height: 18px; border-radius: 50%; background: var(--ink-light); }
  .wordmark__name { font-size: 46px; line-height: 1; }

  .back__brand {
    width: 48%; background: var(--ember-red);
    display: flex; align-items: center; justify-content: center;
  }
  .back__brand .wordmark__name { font-size: 34px; letter-spacing: 3px; }
  .back__brand .wordmark { gap: 10px; }
  .back__brand .wordmark__dot { width: 14px; height: 14px; }

  .back__info {
    flex: 1; background: var(--card-black);
    color: var(--ink-muted); position: relative;
    padding: 46px 0 0 0;
  }
  .contact__name {
    font-weight: 600; font-size: 22px; color: var(--ink-light);
    letter-spacing: 1px; padding-left: 70px; margin-bottom: 34px;
  }
  .contact__list { list-style: none; border-top: 1px solid var(--row-line); }
  .contact__row {
    display: flex; align-items: center; height: 62px;
    border-bottom: 1px solid var(--row-line);
    font-size: 16px; letter-spacing: .5px;
  }
  .contact__row--tall { height: 78px; }
  .contact__icon {
    width: 40px; height: 100%; background: var(--icon-blue);
    display: flex; align-items: center; justify-content: center;
    margin-right: 30px; flex-shrink: 0;
  }
  .contact__icon svg { width: 16px; height: 16px; fill: none; stroke: #fff; stroke-width: 2; }
  .contact__icon-square { width: 12px; height: 12px; background: #fff; }
  .contact__text { line-height: 1.45; }
</style>
</head>
<body>
  <section class="card card--front" aria-label="Card front">
    <div class="front__band">
      <div class="wordmark">
        <span class="wordmark__dot"></span>
        <span class="wordmark__name">Ember Pipe</span>
      </div>
    </div>
  </section>

  <section class="card card--back" aria-label="Card back">
    <div class="back__brand">
      <div class="wordmark">
        <span class="wordmark__dot"></span>
        <span class="wordmark__name">Ember Pipe</span>
      </div>
    </div>
    <div class="back__info">
      <p class="contact__name">Dorian Meltz</p>
      <ul class="contact__list">
        <li class="contact__row contact__row--tall">
          <span class="contact__icon"><svg viewBox="0 0 16 16"><path d="M8 15s5-5 5-9A5 5 0 0 0 3 6c0 4 5 9 5 9z"/><circle cx="8" cy="6" r="1.6"/></svg></span>
          <span class="contact__text">4671 Coppergate Row,<br>Akron OH 40927</span>
        </li>
        <li class="contact__row">
          <span class="contact__icon"><svg viewBox="0 0 16 16"><path d="M3 2h3l1.5 3.5-2 1.3a8 8 0 0 0 3.7 3.7l1.3-2L14 10v3a1 1 0 0 1-1 1A12 12 0 0 1 2 3a1 1 0 0 1 1-1z"/></svg></span>
          <span class="contact__text">555.417.3862</span>
        </li>
        <li class="contact__row">
          <span class="contact__icon"><svg viewBox="0 0 16 16"><rect x="1.5" y="2.5" width="13" height="9" rx="1"/><path d="M5 14h6M8 11.5V14"/></svg></span>
          <span class="contact__text">plorvane.com/epbx</span>
        </li>
        <li class="contact__row">
          <span class="contact__icon"><span class="contact__icon-square"></span></span>
          <span class="contact__text">hearthnet.com/epbx</span>
        </li>
      </ul>
    </div>
  </section>
</body>
</html>
```